VORN Paradigm. the way you communicate in every situation and in all environments.

I would like you to create a diagram depicting a very specific process of communication. it must follow the look of the diagram that i have attached. this is going to be used in a book called LANTERN. it is going to explain the fact that we communicate all the same way using this process as we communicate. it starts with the fact that everyone takes everything that is said personally and then moves on to filters, which is your own agenda or experience kicking in. then you move to your why it matters, which is your motivation and ends with the choice of words you use when you communicate. if you are going to be successful then you must separate the person from the issue.

Target Market(s)

market is executive business people around the world

Industry/Entity Type

Consulting

Font styles to use
Sans Serif

Colors

Designer to choose only greyscale colors for use in the design.

Requirements
Must have
• I would like it to have a diving/ocean/snorkel feel to it. The analogy we are using is to make a deep dive when you are communicating. it must have every part of the diagram you see, it starts at the top with the vorn paradigm (and the words) it then connects to the filters which connects to the why it matters with connects to the words and then end with the separating the person from the issue.
Nice to have
• we are writing a black and white book NO color. therefore the words should be clear and easy to read. Each section should be able to stand on its own so we can write about it separately.
Should not have
• the diagram DOES NOT have to look like the one i gave you. it must explain the fact that it starts with VORN and ends with Separate and must pass through the three areas to get to the SEPARATE.

```html
<!DOCTYPE html>
<html lang="en">
<head>
<meta charset="utf-8">
<title>VORN Paradigm – Communication Dive</title>
<link rel="stylesheet" href="https://fonts.googleapis.com/css2?family=Tinos:wght@400&family=Poppins:ital,wght@1,500&display=swap">
<style>
  :root {
    --water-surface: #e4e4e4;
    --water-top: #c4c4c4;
    --water-mid: #a2a2a2;
    --water-deep: #858585;
    --water-low: #939393;
    --floor-light: #d6d6d6;
    --floor-deep: #bdbdbd;
    --node-fill: #575757;
    --node-fill-dark: #3a3a3a;
    --line-white: #ffffff;
    --title-white: #ffffff;
    --caption-ink: #111111;
  }
  * { margin: 0; padding: 0; box-sizing: border-box; }
  html, body { width: 1200px; height: 763px; overflow: hidden; }
  body { position: relative; background: var(--water-mid); }

  .ocean-backdrop {
    position: absolute; inset: 0;
    background:
      radial-gradient(ellipse 55% 30% at 70% 4%, rgba(255,255,255,0.55), transparent 70%),
      radial-gradient(ellipse 90% 18% at 50% 0%, rgba(255,255,255,0.45), transparent 80%),
      linear-gradient(to bottom,
        var(--water-surface) 0%,
        var(--water-top) 16%,
        var(--water-mid) 38%,
        var(--water-deep) 60%,
        var(--water-low) 76%,
        #a9a9a9 83%,
        var(--floor-light) 90%,
        var(--floor-deep) 100%);
  }

  .light-rays { position: absolute; left: 0; top: 0; width: 1200px; height: 763px; }

  .process-graphic { position: absolute; left: 0; top: 0; width: 1200px; height: 763px; }

  .stage-title {
    position: absolute;
    width: 150px;
    top: 297px;
    text-align: center;
    font-family: "Tinos", "Times New Roman", serif;
    font-size: 23px;
    line-height: 27px;
    color: var(--title-white);
  }

  .stage-caption {
    position: absolute;
    width: 230px;
    top: 474px;
    text-align: center;
    font-family: "Poppins", Arial, sans-serif;
    font-style: italic;
    font-weight: 500;
    font-size: 12.5px;
    line-height: 18px;
    color: var(--caption-ink);
  }
</style>
</head>
<body>
  <div class="ocean-backdrop" role="img" aria-label="Underwater scene with sunlit rippling surface above and sandy sea floor below"></div>

  <svg class="light-rays" viewBox="0 0 1200 763" aria-hidden="true">
    <defs>
      <linearGradient id="ray-fade" x1="0" y1="0" x2="0" y2="1">
        <stop offset="0%" stop-color="#ffffff" stop-opacity="0.45"/>
        <stop offset="60%" stop-color="#ffffff" stop-opacity="0.12"/>
        <stop offset="100%" stop-color="#ffffff" stop-opacity="0"/>
      </linearGradient>
    </defs>
    <g class="sun-beams" fill="url(#ray-fade)">
      <polygon points="700,0 760,0 560,520 500,520"/>
      <polygon points="790,0 830,0 720,460 690,460"/>
      <polygon points="860,0 930,0 900,560 840,560"/>
      <polygon points="960,0 990,0 1060,420 1030,420"/>
      <polygon points="600,0 630,0 380,420 350,420"/>
    </g>
  </svg>

  <svg class="process-graphic" viewBox="0 0 1200 763" aria-hidden="true">
    <defs>
      <radialGradient id="node-gradient" cx="50%" cy="40%" r="60%">
        <stop offset="0%" stop-color="var(--node-fill)"/>
        <stop offset="100%" stop-color="var(--node-fill-dark)"/>
      </radialGradient>
      <g id="stage-node">
        <circle r="86" fill="none" stroke="var(--line-white)" stroke-width="2" stroke-dasharray="7 5"/>
        <circle r="78" fill="none" stroke="var(--line-white)" stroke-width="3"/>
        <circle r="72" fill="url(#node-gradient)"/>
      </g>
      <g id="double-chevron" fill="none" stroke="var(--line-white)" stroke-width="3.5" stroke-linecap="round" stroke-linejoin="round">
        <polyline points="-11,-8 0,1 11,-8"/>
        <polyline points="-11,2 0,11 11,2"/>
      </g>
    </defs>

    <g class="connectors" stroke="var(--line-white)" stroke-width="2.5" fill="var(--line-white)">
      <line x1="235" y1="324" x2="285" y2="324"/><circle cx="238" cy="324" r="6"/>
      <line x1="457" y1="324" x2="510" y2="324"/><circle cx="461" cy="324" r="6"/>
      <line x1="682" y1="324" x2="732" y2="324"/><circle cx="686" cy="324" r="6"/>
      <line x1="904" y1="324" x2="957" y2="324"/><circle cx="908" cy="324" r="6"/>
    </g>

    <use href="#stage-node" x="149" y="324"/>
    <use href="#stage-node" x="371" y="324"/>
    <use href="#stage-node" x="596" y="324"/>
    <use href="#stage-node" x="818" y="324"/>
    <use href="#stage-node" x="1043" y="324"/>

    <use href="#double-chevron" x="149" y="436"/>
    <use href="#double-chevron" x="371" y="436"/>
    <use href="#double-chevron" x="596" y="436"/>
    <use href="#double-chevron" x="818" y="436"/>
    <use href="#double-chevron" x="1043" y="436"/>
  </svg>

  <div class="stage-title" style="left:74px;">VORN<br>Paradigm</div>
  <div class="stage-title" style="left:296px;">Your<br>Filters</div>
  <div class="stage-title" style="left:521px;">Why It<br>Matters</div>
  <div class="stage-title" style="left:743px;">Your<br>Words</div>
  <div class="stage-title" style="left:968px;">What<br>To Do</div>

  <p class="stage-caption" style="left:34px;">When words are taken<br>personally, what<br>happens?</p>
  <p class="stage-caption" style="left:256px;">An accumulation of<br>your experience,<br>knowledge and values</p>
  <p class="stage-caption" style="left:481px;">This is your compass.<br>It is what motivattes<br>you, what drive you.</p>
  <p class="stage-caption" style="left:703px;">This is your immediate<br>response, verbal or<br>perhaps non-verbal</p>
  <p class="stage-caption" style="left:928px;">Separate the Person<br>from the Issue</p>
</body>
</html>
```